Swimming Pool Supply Company Business Cards

We need business cards designed for company. These need to be easy to edit so that we can fill in names, titles, and contact info for each person who works here.

Dalton R. Whitfield
Manager of Legal & Finance
K.L. Brisbane, Incorporated

4837 Grenway Avenue
Marlow Heights, PA 19243

E. dalton@klbrisbane-example.com
M. (215) 555-0173
O. (215) 555-0148

Contact Information for Business Card

Looking to upgrade current business cards with graphic that can be edited. Looking for fresh ideas for an age old industry.

Font styles to use
Serif
Sans Serif

Colors

Designer to choose colors to be used in the design.

Requirements
Must have
• Professional, fresh, unique but professional

```html
<!DOCTYPE html>
<html lang="en">
<head>
<meta charset="utf-8">
<title>K.L. Brisbane Business Cards</title>
<link href="https://fonts.googleapis.com/css2?family=Open+Sans:wght@400;600&display=swap" rel="stylesheet">
<style>
  :root {
    --backdrop: #1d1d1f;
    --card-blue: #3a3ec2;
    --card-blue-deep: #3034a8;
    --silver: #c8cae2;
    --silver-bright: #e4e5f0;
    --silver-soft: #9ea2d8;
  }
  html, body {
    margin: 0;
    padding: 0;
    width: 1200px;
    height: 900px;
    overflow: hidden;
    background: var(--backdrop);
    font-family: "Open Sans", Arial, sans-serif;
  }
  .canvas {
    position: relative;
    width: 1200px;
    height: 900px;
  }
  .card {
    position: absolute;
    left: 250px;
    width: 700px;
    height: 400px;
    border-radius: 8px;
    background: linear-gradient(160deg, var(--card-blue) 0%, var(--card-blue-deep) 100%);
    overflow: hidden;
    color: var(--silver);
  }
  .card--front { top: 35px; }
  .card--back { top: 465px; }

  .brand-name {
    position: absolute;
    margin: 0;
    font-weight: 600;
    letter-spacing: 4px;
    color: var(--silver);
    text-transform: uppercase;
    white-space: nowrap;
  }
  .card--front .brand-name {
    left: 0;
    right: 0;
    top: 120px;
    text-align: center;
    font-size: 72px;
  }
  .card--back .brand-name {
    left: 150px;
    top: 78px;
    font-size: 60px;
  }

  .accent-wedge {
    position: absolute;
    width: 220px;
    height: 14px;
  }
  .card--front .accent-wedge { left: 330px; top: 255px; }
  .card--back .accent-wedge { left: 310px; top: 318px; }

  .web-address {
    position: absolute;
    font-size: 15px;
    color: var(--silver);
    white-space: nowrap;
  }
  .card--front .web-address { left: 330px; top: 285px; }
  .card--back .web-address { left: 330px; top: 346px; }

  .base-stripe {
    position: absolute;
    left: 0;
    right: 0;
    height: 6px;
    background: linear-gradient(90deg, var(--silver-bright) 0%, var(--silver) 45%, var(--silver-soft) 100%);
  }
  .card--front .base-stripe { top: 325px; }
  .card--back .base-stripe { top: 375px; }

  .tagline {
    position: absolute;
    left: 40px;
    top: 22px;
    margin: 0;
    font-size: 25px;
    font-weight: 600;
    color: var(--silver);
    white-space: nowrap;
  }

  .person {
    position: absolute;
    left: 250px;
    top: 168px;
    width: 220px;
    text-align: center;
    font-size: 14px;
    line-height: 20px;
  }
  .person p, .phones p, .address p { margin: 0; }

  .phones {
    position: absolute;
    left: 470px;
    top: 205px;
    font-size: 14px;
    line-height: 20px;
  }
  .address {
    position: absolute;
    left: 110px;
    top: 255px;
    font-size: 14px;
    line-height: 20px;
  }
  .email {
    position: absolute;
    left: 290px;
    top: 292px;
    margin: 0;
    font-size: 14px;
  }
</style>
</head>
<body>
<main class="canvas">

  <section class="card card--front" aria-label="Card front">
    <h1 class="brand-name">Brisbane</h1>
    <svg class="accent-wedge" viewBox="0 0 220 14" aria-hidden="true">
      <polygon points="0,13 220,0 200,5 20,13" fill="#c8cae2"/>
    </svg>
    <div class="web-address">www.klbrisbane-example.com</div>
    <div class="base-stripe"></div>
  </section>

  <section class="card card--back" aria-label="Card back">
    <p class="tagline">Big Enough to Serve You, Small Enough to Care</p>
    <h2 class="brand-name">Brisbane</h2>
    <div class="person">
      <p class="person-name">Dalton R. Whitfield</p>
      <p class="person-title">Manager of Legal &amp; Finance</p>
      <p class="person-company">K.L. Brisbane, Incorporated</p>
    </div>
    <div class="phones">
      <p>M. (215) 555-0173</p>
      <p>O. (215) 555-0148</p>
    </div>
    <div class="address">
      <p>4837 Grenway Avenue</p>
      <p>Marlow Heights, PA 19243</p>
    </div>
    <p class="email">E. dalton@klbrisbane-example.com</p>
    <svg class="accent-wedge" viewBox="0 0 220 14" aria-hidden="true">
      <polygon points="0,13 220,0 200,5 20,13" fill="#c8cae2"/>
    </svg>
    <div class="web-address">www.klbrisbane-example.com</div>
    <div class="base-stripe"></div>
  </section>

</main>
</body>
</html>
```